Paws Of Kindness Business cards

Design a cool, modern business card for my bully breed rescue.

Contact Information for Business Card

Marlene
517-382-4061 Marlene@PawsOfKindnessRescue.net PawsOfKindnessRescue.net

Font styles to use
Serif
Sans Serif

Colors

Designer to choose colors to be used in the design.

Requirements
Must have
• logo and info. Color
Nice to have
• Foil. Maybe some paw prints on the back or some kind of dog illustration.

```html
<!DOCTYPE html>
<html lang="en">
<head>
<meta charset="utf-8">
<title>Paws Of Kindness – Business Cards</title>
<link rel="stylesheet" href="https://fonts.googleapis.com/css2?family=Arimo:wght@400;700&display=swap">
<style>
  :root {
    --paper: #ffffff;
    --card-edge: #c8c8c8;
    --crimson: #be1248;
    --blush: #f4aaaa;
    --wine: #7a0025;
    --ink: #111111;
  }
  html, body {
    margin: 0;
    padding: 0;
    width: 1200px;
    height: 1200px;
    overflow: hidden;
    background: var(--paper);
  }
  .sheet { display: block; width: 1200px; height: 1200px; }
  .card-base { fill: var(--paper); stroke: var(--card-edge); stroke-width: 1; }
  .brand-name {
    font-family: "Arimo", Arial, sans-serif;
    font-weight: 700;
    fill: var(--ink);
  }
  .brand-dot { fill: none; stroke: var(--ink); stroke-width: 4; }
  .brand-dot--small { stroke-width: 1.5; }
  .contact {
    font-family: "Arimo", Arial, sans-serif;
    font-weight: 400;
    fill: var(--ink);
  }
  .faint { opacity: 0.12; }
  .faint-small { opacity: 0.25; }
</style>
</head>
<body>
<svg class="sheet" viewBox="0 0 1500 1500" xmlns="http://www.w3.org/2000/svg">
  <defs>
    <linearGradient id="foil-band" x1="0" y1="0" x2="1" y2="0">
      <stop offset="0" stop-color="var(--crimson)"/>
      <stop offset="0.23" stop-color="var(--crimson)"/>
      <stop offset="0.5" stop-color="var(--blush)"/>
      <stop offset="0.96" stop-color="var(--wine)"/>
      <stop offset="1" stop-color="var(--wine)"/>
    </linearGradient>
  </defs>

  <!-- Front of card -->
  <g class="card card-front" transform="translate(225 60)">
    <rect class="card-base" x="0" y="0" width="1050" height="642"/>
    <polygon class="foil-band" points="0,173 1050,0 1050,467 0,642" fill="url(#foil-band)"/>
    <g class="brand-lockup">
      <circle class="brand-dot" cx="275" cy="85" r="55"/>
      <text class="brand-name" x="275" y="208" font-size="58" text-anchor="middle">Paws Of Kindness</text>
    </g>
    <g class="contact-block" text-anchor="middle">
      <text class="contact" x="752" y="424" font-size="46">Marlene</text>
      <text class="contact" x="752" y="481" font-size="46">517-382-4061</text>
      <text class="contact" x="735" y="536" font-size="34">Marlene@PawsOfKindnessRescue.net</text>
      <text class="contact" x="752" y="594" font-size="42">PawsOfKindnessRescue.net</text>
    </g>
  </g>

  <!-- Back of card -->
  <g class="card card-back" transform="translate(225 798)">
    <rect class="card-base" x="0" y="0" width="1050" height="642"/>
    <polygon class="foil-band" points="0,174 1050,0 1050,469 0,642" fill="url(#foil-band)"/>
    <g class="brand-lockup faint">
      <circle class="brand-dot" cx="525" cy="220" r="55"/>
      <text class="brand-name" x="525" y="345" font-size="58" text-anchor="middle">Paws Of Kindness</text>
    </g>
    <g class="brand-lockup faint-small">
      <circle class="brand-dot brand-dot--small" cx="84" cy="56" r="12"/>
      <text class="brand-name" x="84" y="82" font-size="12" text-anchor="middle">Paws Of Kindness</text>
    </g>
    <g class="brand-lockup faint-small">
      <circle class="brand-dot brand-dot--small" cx="944" cy="559" r="12"/>
      <text class="brand-name" x="944" y="585" font-size="12" text-anchor="middle">Paws Of Kindness</text>
    </g>
  </g>
</svg>
</body>
</html>
```